Price Package PDF - 2 page PDF of stylized price packages for property management firm

Looking for a 2 x A4 page PDF for our two price packages.
I would like this to be in similar style to our website www.harbourlanerentals.com.au
I have attached an example. But would like mine to be a little more stylish and modern, preferably using design similar to our website.
Words and images also attached

Target Market(s)

investment property owners, male and female, aged 30-60

Industry/Entity Type

Real Estate

Font styles to use
Sans Serif

Requirements
Must have
• split two packages onto seperate A4 pages (See example file attached)
• Contact info:
• Website: www.harbourlanerentals.com.au
• email: info@harbourlanerentals.com.au
• Phone: Tom Radley 0417 562 903, Larisa Okonjo 0409 317 648
• Office Address: Suite 7, 12-14 Wattle Parade, Curl Curl NSW 2096
Nice to have
• I would like to use any of the pictures provided or images of modern residential property interior or of Sydney's Northern Beaches.

```html
<!DOCTYPE html>
<html lang="en">
<head>
<meta charset="utf-8">
<title>Harbour Lane Rentals – Price Packages</title>
<link rel="stylesheet" href="https://fonts.googleapis.com/css2?family=Mulish:wght@300;400;600;700;800&display=swap">
<style>
  :root {
    --backdrop: #0f111a;
    --paper: #ffffff;
    --panel: #2d3140;
    --row-dark: #3b4252;
    --row-mid: #4d5869;
    --row-light: #5a6577;
    --ink: #2a2e3b;
    --list-ink: #d9dde4;
    --white: #ffffff;
  }
  * { box-sizing: border-box; margin: 0; padding: 0; }
  html, body { width: 1200px; height: 814px; overflow: hidden; }
  body {
    background: var(--backdrop);
    font-family: "Mulish", sans-serif;
    position: relative;
  }
  .page {
    position: absolute;
    top: 42px;
    width: 516px;
    height: 730px;
    background: var(--paper);
    overflow: hidden;
  }
  .page--all { left: 81px; }
  .page--lease { left: 614px; }

  .hero {
    position: absolute;
    left: 0; top: 0;
    width: 516px; height: 411px;
  }
  .page--all .hero {
    background: linear-gradient(180deg, #4fe9bd 0%, #5fe6c0 35%, #3fa879 65%, #2f7c55 100%);
  }
  .page--lease .hero {
    background: linear-gradient(160deg, #173a8c 0%, #1f67a8 30%, #3fd8b8 60%, #2e9a86 85%, #1b5b55 100%);
  }
  .brand {
    position: absolute;
    left: 0; right: 0; top: 58px;
    text-align: center;
    color: var(--white);
    font-weight: 700;
    font-size: 27px;
    letter-spacing: 0.5px;
    white-space: nowrap;
  }

  .title-band {
    position: absolute;
    left: 0; top: 411px;
    width: 516px; height: 53px;
    display: flex; align-items: center; justify-content: center;
    text-align: center;
    white-space: nowrap;
    color: var(--ink);
    font-weight: 300;
    font-size: 29px;
    letter-spacing: 0.3px;
  }
  .page--lease .title-band {
    font-size: 25.5px;
    letter-spacing: 0.2px;
  }

  .details {
    position: absolute;
    left: 0; top: 464px;
    width: 516px; height: 214px;
    background: var(--panel);
  }
  .includes {
    position: absolute;
    left: 22px; top: 13px;
    color: var(--list-ink);
    font-size: 7.6px;
    line-height: 11.2px;
  }
  .includes__title {
    font-size: 8px;
    font-weight: 800;
    color: var(--white);
    line-height: 11px;
  }
  .includes li { list-style: none; padding-left: 5px; text-indent: -4px; white-space: nowrap; }
  .includes li::before { content: "· "; }
  .includes .cont { padding-left: 5px; text-indent: 0; }
  .includes .cont::before { content: ""; }

  .rates {
    position: absolute;
    left: 289px; top: 10px;
    width: 204px; height: 194px;
    background: var(--paper);
  }
  .rates li {
    list-style: none;
    height: 19.9px;
    display: flex; align-items: center;
    padding-left: 14px;
    font-size: 7.4px;
    white-space: nowrap;
    color: var(--list-ink);
  }
  .rates .rates__head { background: var(--paper); color: var(--ink); font-weight: 800; font-size: 7.8px; }
  .rates .rates__key { background: var(--row-dark); color: var(--white); font-weight: 800; }
  .rates .rates__row:nth-child(odd) { background: var(--row-mid); }
  .rates .rates__row:nth-child(even) { background: var(--row-light); }

  .footer {
    position: absolute;
    left: 0; top: 678px;
    width: 516px; height: 52px;
    display: flex; flex-direction: column; align-items: center; justify-content: center;
    gap: 7px;
    color: var(--ink);
    font-size: 7.4px;
    font-weight: 800;
    white-space: nowrap;
  }
</style>
</head>
<body>

<section class="page page--all">
  <div class="hero" role="img" aria-label="Photo of modern terraced townhouses with lush gardens and stairs under a bright sky, teal-tinted"></div>
  <div class="brand">HARBOUR LANE RENTALS</div>
  <h2 class="title-band">ALL INCLUSIVE PACKAGE</h2>
  <div class="details">
    <div class="includes">
      <h3 class="includes__title">INCLUDES</h3>
      <ul>
        <li>Securing Tenant</li>
        <li>Reference/Database Checking</li>
        <li>Lease Preparation and Signing</li>
        <li>Direct Debit rent collection</li>
        <li>Zero arrears policy management</li>
        <li>Payment of Rates and levies</li>
        <li>Insurance management</li>
        <li>Coordination or all repairs and maintenance</li>
        <li>Regular rent reviews and renewals</li>
        <li>Detailed ingoing, ongoing and outgoing inspections with photos</li>
        <li class="cont">and videos / viewable through your personal Landlord portal</li>
        <li>Bond management – lodging and refunding</li>
        <li>Electronic monthly and EOFY statements</li>
        <li>Annual scheduled maintenance report</li>
        <li>Regulation/compliance management</li>
        <li>Tribunal Representation</li>
      </ul>
    </div>
    <ul class="rates">
      <li class="rates__head">ALL INCLUSIVE PACKAGE</li>
      <li class="rates__key">Management Rate: 10% + GST of rental income</li>
      <li class="rates__row">Letting Fee: No Charge</li>
      <li class="rates__row">Advertising: No Charge</li>
      <li class="rates__row">Professional Photography: $199 (inc GST) 4 x Photos</li>
      <li class="rates__row">Statements: No Charge</li>
      <li class="rates__row">Lease Preperation: No Charge</li>
      <li class="rates__row">Renewal Fees: No Charge</li>
    </ul>
  </div>
  <footer class="footer">
    <p>Suite 7, 12-14 Wattle Parade, Curl Curl NSW 2096 | Tom Radley 0417 562 903 - Larisa Okonjo 0409 317 648</p>
    <p>www.harbourlanerentals.com.au | info@harbourlanerentals.com.au</p>
  </footer>
</section>

<section class="page page--lease">
  <div class="hero" role="img" aria-label="Photo of a harbourside ferry wharf building with large rooftop letters against a deep blue sky, teal-tinted"></div>
  <div class="brand">HARBOUR LANE RENTALS</div>
  <h2 class="title-band">LEASE AND MANAGEMENT PACKAGE</h2>
  <div class="details">
    <div class="includes">
      <h3 class="includes__title">INCLUDES</h3>
      <ul>
        <li>Securing Tenant</li>
        <li>Reference/Database Checking</li>
        <li>Lease Preparation and Signing</li>
        <li>Direct Debit rent collection</li>
        <li>Zero arrears policy management</li>
        <li>Payment of Rates and levies</li>
        <li>Insurance management</li>
        <li>Coordination or all repairs and maintenance</li>
        <li>Regular rent reviews and renewals</li>
        <li>Detailed ingoing, ongoing and outgoing inspections with photos</li>
        <li class="cont">and videos / viewable through your personal Landlord portal</li>
        <li>Bond management – lodging and refunding</li>
        <li>Electronic monthly and EOFY statements</li>
        <li>Annual scheduled maintenance report</li>
        <li>Regulation/compliance management</li>
        <li>Tribunal Representation</li>
      </ul>
    </div>
    <ul class="rates">
      <li class="rates__head">MANAGEMENT RATE</li>
      <li class="rates__key">Management Rate: 6% +GST of rental income</li>
      <li class="rates__row">Letting Fee: 1 weeks rent +GST 6 or 12 month lease</li>
      <li class="rates__row">Advertising: $350 (Inc GST)</li>
      <li class="rates__row">Professional Photography: $199 (inc GST) 4 x Photos</li>
      <li class="rates__row">Statements: $5.00 Per month</li>
      <li class="rates__row">Lease Preperation: No Charge</li>
      <li class="rates__row">Renewal Fees: ½ Weeks Rent +GST</li>
    </ul>
  </div>
  <footer class="footer">
    <p>Suite 7, 12-14 Wattle Parade, Curl Curl NSW 2096 | Tom Radley 0417 562 903 - Larisa Okonjo 0409 317 648</p>
    <p>www.harbourlanerentals.com.au | info@harbourlanerentals.com.au</p>
  </footer>
</section>

</body>
</html>
```